Business card

I need to make clear the my status by my works acceptance in academia and pop culture.

The format of the card in the pics uploaded is an approximation. Something new may work or you make just tweak this design to make it more powerful.

```html
<!DOCTYPE html>
<html lang="en">
<head>
<meta charset="utf-8">
<title>Leon Marwick, Ph.D — Business Card</title>
<link href="https://fonts.googleapis.com/css2?family=Bebas+Neue&family=Roboto:ital,wght@0,400;0,500;0,700;0,900;1,400;1,700&display=swap" rel="stylesheet">
<style>
  :root {
    --backdrop: #7b5c3e;
    --card-light: #f0f0f0;
    --card-dark: #1e1e1e;
    --ink-dark: #1c1c1c;
    --ink-light: #ffffff;
    --ink-soft: #d9d9d9;
    --quote-grey: #b4b4b4;
    --quote-grey-dark: #c8c8c8;
  }
  * { margin: 0; padding: 0; box-sizing: border-box; }
  html, body { width: 900px; height: 1200px; overflow: hidden; }
  body {
    background: var(--backdrop);
    font-family: "Roboto", Arial, sans-serif;
    position: relative;
  }
  .card {
    position: absolute;
    border-radius: 22px;
    box-shadow: 0 10px 28px rgba(0,0,0,0.35);
  }
  .card--front { left: 72px; top: 135px; width: 773px; height: 448px; background: var(--card-light); color: var(--ink-dark); }
  .card--back { left: 75px; top: 625px; width: 772px; height: 447px; background: var(--card-dark); color: var(--ink-light); }

  .quote-mark { position: absolute; }
  .card--front .quote-mark { left: 50px; top: 60px; width: 142px; height: 110px; }
  .card--back .quote-mark { left: 52px; top: 54px; width: 102px; height: 78px; }

  .name {
    position: absolute; left: 327px; top: 54px;
    font-family: "Bebas Neue", "Oswald", sans-serif;
    font-size: 67px; line-height: 65px; letter-spacing: 1px;
  }
  .tagline {
    position: absolute; left: 48px;
    font-weight: 700; font-style: italic; font-size: 20px; line-height: 26px;
  }
  .tagline--status { top: 219px; }
  .tagline--prize { top: 336px; }
  .exhibition {
    position: absolute; left: 327px; top: 219px; width: 400px;
    font-weight: 700; font-style: italic; font-size: 20px; line-height: 26px;
  }
  .web {
    position: absolute; left: 325px; top: 336px;
    font-weight: 500; font-size: 23px; line-height: 28px; letter-spacing: 4.2px;
  }

  .headline {
    position: absolute; left: 50px; top: 150px;
    font-weight: 700; font-style: italic; font-size: 33px; line-height: 42px;
  }
  .contact {
    position: absolute; left: 46px; top: 340px;
    font-weight: 500; font-size: 23px; line-height: 31px;
  }
  .works { position: absolute; left: 403px; top: 50px; width: 350px; }
  .works__title { font-weight: 700; font-size: 20px; line-height: 26px; }
  .works__list { list-style: none; margin-top: 24px; }
  .works__list li {
    font-size: 21px; line-height: 31px; padding-left: 19px; position: relative;
  }
  .works__list li::before {
    content: ""; position: absolute; left: 2px; top: 12px;
    width: 8px; height: 8px; border-radius: 50%; background: var(--ink-light);
  }
  .works__sub { font-style: italic; font-size: 20px; color: var(--ink-soft); margin-top: 14px; line-height: 26px; }
  .works__list--films { margin-top: 18px; }
  .works__list--films li { padding-left: 23px; }
</style>
</head>
<body>

<section class="card card--front">
  <svg class="quote-mark" viewBox="0 0 142 110" aria-hidden="true">
    <g fill="var(--quote-grey)">
      <path d="M30 110 C12 110 0 96 0 78 C0 40 22 12 58 0 L64 12 C44 22 34 36 33 50 C50 50 62 63 62 80 C62 97 48 110 30 110 Z"/>
      <path d="M108 110 C90 110 78 96 78 78 C78 40 100 12 136 0 L142 12 C122 22 112 36 111 50 C128 50 140 63 140 80 C140 97 126 110 108 110 Z"/>
    </g>
  </svg>
  <h1 class="name">Leon<br>Marwick, Ph.D</h1>
  <p class="tagline tagline--status">The Keystone and<br>Compass of Psychology<br>&amp; History</p>
  <p class="tagline tagline--prize">The Grand Laurel Prize is<br>a Sure Thing.</p>
  <p class="exhibition">A Royal Heritage Museum Exhibition Featured Leon’s Ideas. Leon’s Bio-Sociology Has Restructured the Liberal Arts</p>
  <p class="web">For Canonical Status<br>www.leon-marwick.org</p>
</section>

<section class="card card--back">
  <svg class="quote-mark" viewBox="0 0 142 110" aria-hidden="true">
    <g fill="var(--quote-grey-dark)">
      <path d="M30 110 C12 110 0 96 0 78 C0 40 22 12 58 0 L64 12 C44 22 34 36 33 50 C50 50 62 63 62 80 C62 97 48 110 30 110 Z"/>
      <path d="M108 110 C90 110 78 96 78 78 C78 40 100 12 136 0 L142 12 C122 22 112 36 111 50 C128 50 140 63 140 80 C140 97 126 110 108 110 Z"/>
    </g>
  </svg>
  <p class="headline">Leon Maybe the<br>Greatest Genius<br>in History</p>
  <p class="contact">555-014-0277<br>sageleon@postmail.net</p>
  <div class="works">
    <p class="works__title">Leon’s Bio-Psych is<br>Fundamental To All Museums<br>Such As:</p>
    <ul class="works__list">
      <li>The Galerie Mirelle</li>
      <li>The Harborview Museum</li>
      <li>The Castellan Archive</li>
    </ul>
    <p class="works__sub">and the films:</p>
    <ul class="works__list works__list--films">
      <li>Starfall Sentinel 1986</li>
      <li>Kira Vale and The Final Ember</li>
      <li>Delta River Run</li>
    </ul>
  </div>
</section>

</body>
</html>
```